Managed Services Provider for Medical Practices Business Card Design

We need a business card design for a new company based in the Illawarra region on NSW Australia, with intentions of expanding further into other regions. We provide I.T. managed services, server, printer, phone and hardware procurement and installations. We specialise in Medical Practices e.g. General Practitioners, Surgeons and other medical specialists etc. We would like to see colours that theme with our website. The final design should communicate integrity, strength, security and reliability.

Security

Velbrook Omnilux, Dorian Pakula, Shop 9 Cardwell Arcade, 517 Fenwick Orchard Road Marlowe NSW 2694, Partner - Senior Technician, Ph: 0488 371 590, Email: dorian@omnilux.net.au, Web: www.omnilux.net.au

Velbrook Omnilux, Evan Brockwirth, Shop 9 Cardwell Arcade, 517 Fenwick Orchard Road Marlowe NSW 2694, Partner - Senior Technician, Ph: 0461 937 025, Email: evan@omnilux.net.au, Web: www.omnilux.net.au

```html
<!DOCTYPE html>
<html lang="en">
<head>
<meta charset="utf-8">
<title>Velbrook Omnilux – Business Card</title>
<link rel="stylesheet" href="https://fonts.googleapis.com/css2?family=Open+Sans:wght@400;600;700;800&display=swap">
<style>
  :root {
    --brand-green: #58bb47;
    --ink: #1d1d1d;
    --paper: #ffffff;
    --backdrop: #b9b9b9;
    --card-w: 600px;
    --card-h: 343px;
  }
  * { box-sizing: border-box; margin: 0; padding: 0; }
  html, body {
    width: 1200px; height: 900px; overflow: hidden;
    background: var(--backdrop);
    font-family: "Open Sans", Arial, sans-serif;
  }
  .canvas { position: relative; width: 1200px; height: 900px; }
  .card {
    position: absolute;
    width: var(--card-w); height: var(--card-h);
    overflow: hidden;
  }
  .card--front { left: 90px; top: 90px; background: var(--brand-green); }
  .card--back { left: 510px; top: 470px; background: var(--paper); }

  .wordmark {
    position: absolute;
    font-weight: 800;
    letter-spacing: -0.5px;
    line-height: 1;
    white-space: nowrap;
  }
  .tagline {
    position: absolute;
    font-weight: 400;
    white-space: nowrap;
    line-height: 1;
  }
  .card--front .wordmark { right: 40px; top: 140px; font-size: 50px; color: var(--paper); }
  .card--front .tagline { right: 40px; top: 202px; font-size: 20px; color: var(--paper); }

  .card--back .wordmark { right: 30px; top: 46px; font-size: 42px; color: var(--brand-green); }
  .card--back .tagline { right: 30px; top: 98px; font-size: 18px; color: var(--brand-green); }

  .name-tab {
    position: absolute; left: 182px; top: 150px; width: 10px; height: 24px;
    background: var(--brand-green);
    transform: skewY(20deg);
  }
  .name-band {
    position: absolute; left: 200px; right: 0; top: 158px; height: 24px;
    background: var(--brand-green);
  }
  .person-name {
    position: absolute; left: 214px; top: 160px;
    font-size: 16px; font-weight: 700; color: var(--ink);
    text-transform: uppercase; letter-spacing: 0.5px; line-height: 20px;
  }
  .person-role {
    position: absolute; left: 214px; top: 189px;
    font-size: 13px; color: var(--ink);
  }
  .contact-list {
    position: absolute; left: 200px; top: 216px;
    list-style: none; font-size: 14px; color: var(--ink);
  }
  .contact-list li { display: flex; align-items: center; gap: 8px; height: 23px; }
  .contact-icon { width: 12px; height: 12px; flex: none; }
  .address {
    position: absolute; right: 30px; top: 226px;
    font-size: 11px; font-weight: 700; font-style: normal; color: var(--brand-green);
    text-transform: uppercase; text-align: right; line-height: 19px; letter-spacing: 0.3px;
  }
  .base-bar {
    position: absolute; left: 180px; right: 0; bottom: 26px; height: 8px;
    background: var(--brand-green);
  }
</style>
</head>
<body>
<main class="canvas">
  <section class="card card--front" aria-label="Card front">
    <p class="wordmark">Velbrook Omnilux</p>
    <p class="tagline">your technical specialists</p>
  </section>

  <section class="card card--back" aria-label="Card back">
    <p class="wordmark">Velbrook Omnilux</p>
    <p class="tagline">your technical specialists</p>

    <div class="name-tab"></div>
    <div class="name-band"></div>
    <p class="person-name">Dorian Pakula</p>
    <p class="person-role">Partner - Senior Technician</p>

    <ul class="contact-list">
      <li>
        <svg class="contact-icon" viewBox="0 0 12 12" aria-hidden="true"><rect width="12" height="12" rx="2" fill="#58bb47"/><rect x="4" y="2" width="4" height="8" rx="1" fill="#fff"/></svg>
        0488 371 590
      </li>
      <li>
        <svg class="contact-icon" viewBox="0 0 12 12" aria-hidden="true"><rect width="12" height="12" rx="2" fill="#58bb47"/><rect x="2" y="3.5" width="8" height="5" fill="#fff"/><path d="M2 3.5 6 6.5 10 3.5" stroke="#58bb47" fill="none" stroke-width="0.8"/></svg>
        dorian@omnilux.net.au
      </li>
      <li>
        <svg class="contact-icon" viewBox="0 0 12 12" aria-hidden="true"><rect width="12" height="12" rx="2" fill="#58bb47"/><circle cx="6" cy="6" r="3.5" fill="none" stroke="#fff"/><path d="M2.5 6h7M6 2.5v7" stroke="#fff" stroke-width="0.8"/></svg>
        www.omnilux.net.au
      </li>
    </ul>

    <address class="address">
      Shop 9 Cardwell Arcade<br>
      517 Fenwick Orchard<br>
      Road Marlowe NSW 2694
    </address>

    <div class="base-bar"></div>
  </section>
</main>
</body>
</html>
```